Kelvo Fitness Personal Training Business

I need a business card design with a logo for my personal training company. I'd like the colors to be a vibrant green and black. I'd like the logo to incorporate an anvil (or something similar). I train hardcore competitive athletes as well as soccer moms trying to get and/or stay in shape. I need a logo that will not pigeon hole me in one category or the other, but at the same time not be too intimidating to soccer moms, but will not be off putting to the more hardcore trainees. The design should be attention grabbing and aesthetic.
Target Market(s)
Hardcore athletes as well as average people just trying to get/stay in shape.
Industry/Entity Type
Training
Look and feel

```html
<!DOCTYPE html>
<html lang="en">
<head>
<meta charset="utf-8">
<title>Kelvo Fitness – Business Card</title>
<link rel="stylesheet" href="https://fonts.googleapis.com/css2?family=Figtree:wght@400;600&family=Barlow+Semi+Condensed:wght@300;400&family=Saira+Condensed:wght@600&display=swap">
<style>
  :root {
    --card-bg: #161616;
    --card-bg-light: #222222;
    --lime: #d4e021;
    --flame: #f0522a;
    --steel: #bdbdbf;
    --frame: #7a7a7a;
  }
  * { margin: 0; padding: 0; box-sizing: border-box; }
  html, body {
    width: 686px;
    height: 1200px;
    overflow: hidden;
    background: var(--card-bg);
  }
  .card {
    position: relative;
    width: 686px;
    height: 1200px;
    background: radial-gradient(ellipse at 50% 35%, var(--card-bg-light) 0%, var(--card-bg) 75%);
    overflow: hidden;
  }
  .card__frame {
    position: absolute;
    inset: 23px;
    border: 2px solid var(--frame);
  }
  .centered {
    position: absolute;
    left: 0;
    width: 100%;
    text-align: center;
    transform: translateY(-50%);
    white-space: nowrap;
  }
  .brand-name {
    top: 150px;
    font-family: "Saira Condensed", sans-serif;
    font-weight: 600;
    font-size: 80px;
    letter-spacing: 2px;
    color: var(--lime);
    text-transform: uppercase;
  }
  .brand-mark {
    position: absolute;
    left: 50%;
    top: 350px;
    width: 170px;
    height: 170px;
    margin: -85px 0 0 -85px;
    border-radius: 50%;
    background: var(--steel);
  }
  .tagline-rule {
    position: absolute;
    left: 80px;
    width: 524px;
    height: 2px;
    background: var(--lime);
  }
  .tagline-rule--top { top: 490px; }
  .tagline-rule--bottom { top: 560px; }
  .tagline {
    top: 526px;
    font-family: "Figtree", sans-serif;
    font-weight: 600;
    font-size: 42px;
    letter-spacing: 3px;
    color: var(--flame);
    text-transform: uppercase;
  }
  .trainer-name {
    top: 714px;
    font-family: "Figtree", sans-serif;
    font-weight: 400;
    font-size: 42px;
    color: var(--lime);
  }
  .trainer-title {
    top: 762px;
    font-family: "Barlow Semi Condensed", sans-serif;
    font-weight: 300;
    font-size: 36px;
    color: var(--steel);
    text-transform: uppercase;
  }
  .divider-diamond {
    position: absolute;
    left: 50%;
    top: 864px;
    width: 24px;
    height: 24px;
    margin: -12px 0 0 -12px;
    background: var(--flame);
    transform: rotate(45deg);
  }
  .contact-phone {
    top: 984px;
    font-family: "Figtree", sans-serif;
    font-size: 37px;
    color: var(--lime);
  }
  .contact-email {
    top: 1031px;
    font-family: "Figtree", sans-serif;
    font-size: 34px;
    color: var(--lime);
  }
  .contact-address {
    top: 1120px;
    font-family: "Barlow Semi Condensed", sans-serif;
    font-weight: 300;
    font-size: 36px;
    color: var(--steel);
    text-transform: uppercase;
  }
</style>
</head>
<body>
  <main class="card">
    <div class="card__frame"></div>

    <header class="brand">
      <div class="centered brand-name">Kelvo Fitness</div>
      <div class="brand-mark" aria-hidden="true"></div>
      <div class="tagline-rule tagline-rule--top"></div>
      <div class="centered tagline">Personal Training</div>
      <div class="tagline-rule tagline-rule--bottom"></div>
    </header>

    <section class="trainer">
      <div class="centered trainer-name">Marcus Hale</div>
      <div class="centered trainer-title">Professional Trainer</div>
    </section>

    <div class="divider-diamond" aria-hidden="true"></div>

    <footer class="contact">
      <div class="centered contact-phone">555-318-2046</div>
      <div class="centered contact-email">marcus@kelvofitness.com</div>
      <div class="centered contact-address">482 Summit Avenue, Riverton, US 20417</div>
    </footer>
  </main>
</body>
</html>
```